Professional violinist needs business cards

I am trying to attract the following jobs:
-private violin lessons (primarily classical)
-performance gigs (weddings, birthday parties, funerals, etc.)
-collaborations with other artists (studio recordings, performances)

I want to communicate that I have a very high standard of excellence for my work, but I also love people and celebrations.
Values/style words I like are:
love, joy, peace, fun, beauty, authenticity, excellence, warmth, refined/sleek, free spirited. If that's too confusing, just ignore :)

I will attach my favorite business card template that I could find on Canva. The lines are supposed to be like a music staff, which I think is really cool, but I also don't want it to look too busy. I like the simple black and white--I think it looks sharp--but I also am open to other ideas. I also have seen business cards with pictures included that looked great, so I attached an image that could be used as well.

I am also attaching a file that I made of my initials that could be used as a logo, but I'm not sure if it should be included.

Information on the card:
-My name (18 letters total)
-"violinist"
-phone number, email, website

Thank you!

```html
<!DOCTYPE html>
<html lang="en">
<head>
<meta charset="utf-8">
<title>Marielle Haverford — Violinist Business Cards</title>
<link href="https://fonts.googleapis.com/css2?family=Dancing+Script:wght@500&family=Cinzel:wght@500&family=EB+Garamond:wght@400&display=swap" rel="stylesheet">
<style>
  :root {
    --backdrop: #2b2b2b;
    --card-dark: #23262a;
    --card-dark-edge: #1d2024;
    --staff-line: rgba(255,255,255,0.14);
    --gold: #d3c2a0;
    --ivory: #ebe7df;
    --stone-1: #3a3a3a;
    --stone-2: #242424;
    --photo-1: #1a1614;
    --photo-2: #5a3320;
  }
  * { margin: 0; padding: 0; box-sizing: border-box; }
  html, body { width: 1200px; height: 1138px; overflow: hidden; background: var(--backdrop); }
  .sheet { position: relative; width: 1200px; height: 1138px; }

  .card {
    position: absolute;
    border-radius: 14px;
    overflow: hidden;
    box-shadow: 0 6px 14px rgba(0,0,0,0.45);
  }
  .card--front {
    left: 274px; top: 186px; width: 622px; height: 376px;
    background: linear-gradient(160deg, var(--card-dark) 0%, var(--card-dark-edge) 100%);
  }
  .card--back {
    left: 276px; top: 608px; width: 618px; height: 374px;
    background: var(--stone-2);
  }

  .staff { position: absolute; left: 0; width: 100%; height: 1px; background: var(--staff-line); }

  .brand-mark {
    position: absolute;
    display: flex; align-items: center; justify-content: center; gap: 10px;
    font-family: "Cinzel", serif; font-weight: 500;
    color: var(--gold); letter-spacing: 2px; line-height: 1; white-space: nowrap;
  }
  .brand-dot {
    width: 12px; height: 12px; border-radius: 50%;
    background: var(--gold); flex: none;
  }
  .card--front .brand-mark {
    left: 0; width: 100%; top: 112px; height: 30px; font-size: 20px;
  }
  .card--front .brand-mark .brand-text { background: var(--card-dark); padding: 4px 6px; }
  .card--back .brand-mark {
    left: 256px; width: 340px; top: 80px; height: 28px; font-size: 17px;
  }

  .name {
    position: absolute; text-align: center;
    font-family: "Dancing Script", cursive; font-weight: 500;
    color: var(--ivory); line-height: 1; white-space: nowrap;
  }
  .card--front .name { left: 0; width: 100%; top: 208px; font-size: 38px; }
  .card--back .name { left: 256px; width: 340px; top: 142px; font-size: 34px; }

  .role {
    position: absolute; text-align: center;
    font-family: "Cinzel", serif; font-weight: 500;
    color: var(--ivory); letter-spacing: 3px; line-height: 1;
  }
  .card--front .role { left: 0; width: 100%; top: 257px; font-size: 18px; }
  .card--back .role {
    left: 282px; width: 300px; top: 182px; font-size: 17px;
    display: flex; align-items: center; justify-content: center; gap: 18px;
  }
  .role-rule { width: 70px; height: 1px; background: linear-gradient(90deg, transparent, var(--gold)); }
  .role-rule--right { background: linear-gradient(90deg, var(--gold), transparent); }

  .portrait {
    position: absolute; left: 0; top: 0; width: 250px; height: 100%;
    background: radial-gradient(ellipse at 40% 55%, var(--photo-2) 0%, var(--photo-1) 55%);
  }
  .stone-wall {
    position: absolute; left: 220px; top: 0; right: 0; bottom: 0;
    background: linear-gradient(135deg, var(--stone-1) 0%, var(--stone-2) 100%);
  }

  .contact {
    position: absolute; left: 282px; width: 300px; top: 226px;
    list-style: none; text-align: center;
    font-family: "EB Garamond", serif; font-size: 16px; line-height: 23.5px;
    color: var(--ivory);
  }
  .contact .domain { color: var(--gold); }
</style>
</head>
<body>
<main class="sheet">
  <section class="card card--front" aria-label="Business card front">
    <div class="staff" style="top:92px"></div>
    <div class="staff" style="top:115px"></div>
    <div class="staff" style="top:138px"></div>
    <div class="staff" style="top:162px"></div>
    <div class="brand-mark"><span class="brand-dot"></span><span class="brand-text">Haverford Strings</span></div>
    <h1 class="name">Marielle Haverford</h1>
    <p class="role">VIOLINIST</p>
  </section>

  <section class="card card--back" aria-label="Business card back">
    <div class="stone-wall" role="img" aria-label="Dark stacked stone wall texture"></div>
    <div class="portrait" role="img" aria-label="Violinist in a black dress holding a violin and bow at her side"></div>
    <div class="brand-mark"><span class="brand-dot"></span><span class="brand-text">Haverford Strings</span></div>
    <h2 class="name">Marielle Haverford</h2>
    <p class="role"><span class="role-rule"></span>VIOLINIST<span class="role-rule role-rule--right"></span></p>
    <ul class="contact">
      <li>+12 (555) 014-2736</li>
      <li>Marielle@MarielleHaverford.com</li>
      <li>www.<span class="domain">MarielleHaverford</span>.com</li>
      <li>Portland, OR</li>
    </ul>
  </section>
</main>
</body>
</html>
```